Networking card

I just need a simple design with the following information:
Milan Dorsey
415.608.2931
mdorsey083651@quillpost.example

I would like to have a white background with blue text like in this sample: https://lumacardstudio.example/business-card-527306/

```html
<!DOCTYPE html>
<html lang="en">
<head>
<meta charset="utf-8">
<title>Milan Dorsey – Networking Card</title>
<link href="https://fonts.googleapis.com/css2?family=Montserrat:wght@400;600&display=swap" rel="stylesheet">
<style>
  :root {
    --brand-blue: #06467a;
    --card-white: #ffffff;
    --ink: #1c1c1c;
    --backdrop: #e6e7e9;
  }
  * { margin: 0; padding: 0; box-sizing: border-box; }
  html, body {
    width: 1200px;
    height: 1200px;
    overflow: hidden;
    background: var(--backdrop);
    font-family: "Montserrat", sans-serif;
  }
  .business-card {
    position: absolute;
    left: 100px;
    top: 314px;
    width: 1000px;
    height: 572px;
    background: var(--card-white);
    border-radius: 44px;
    box-shadow: 0 3px 0 var(--brand-blue), 0 18px 40px rgba(0,0,0,0.18);
    overflow: hidden;
  }
  .name-band {
    position: absolute;
    left: 0;
    top: 190px;
    width: 600px;
    height: 88px;
    background: var(--brand-blue);
  }
  .holder-name {
    position: absolute;
    right: 44px;
    bottom: 8px;
    color: var(--card-white);
    font-weight: 600;
    font-size: 58px;
    letter-spacing: 1px;
    text-transform: uppercase;
    line-height: 1;
    white-space: nowrap;
  }
  .contact-list {
    position: absolute;
    left: 250px;
    top: 296px;
    list-style: none;
  }
  .contact-item {
    display: flex;
    align-items: center;
    gap: 18px;
    height: 56px;
    margin-bottom: 10px;
    font-size: 34px;
    color: var(--ink);
    white-space: nowrap;
  }
  .contact-icon {
    width: 48px;
    height: 48px;
    flex: none;
  }
</style>
</head>
<body>
  <section class="business-card">
    <div class="name-band">
      <h1 class="holder-name">Milan Dorsey</h1>
    </div>
    <ul class="contact-list">
      <li class="contact-item">
        <svg class="contact-icon" viewBox="0 0 48 48" aria-hidden="true">
          <circle cx="24" cy="24" r="24" fill="var(--brand-blue)"/>
          <path d="M17 13c1.5-1 3-.5 3.6.8l1.7 3.8c.4 1-.1 2-1 2.5l-1.6.9c1 2.8 3.3 5.4 6.1 6.8l1-1.5c.6-.9 1.7-1.2 2.6-.7l3.6 2c1.2.7 1.5 2.2.5 3.5l-1.4 1.8c-1 1.2-2.7 1.6-4.3 1C20 32.4 15 26.6 13.4 19.8c-.4-1.6.1-3.2 1.3-4.3z" fill="#fff"/>
        </svg>
        <span class="contact-text">415.608.2931</span>
      </li>
      <li class="contact-item">
        <svg class="contact-icon" viewBox="0 0 48 48" aria-hidden="true">
          <circle cx="24" cy="24" r="24" fill="var(--brand-blue)"/>
          <rect x="12" y="16" width="24" height="16" rx="1.5" fill="#fff"/>
          <path d="M12.5 16.8 24 26l11.5-9.2M12.5 31.2l8.5-7.5M35.5 31.2l-8.5-7.5" fill="none" stroke="var(--brand-blue)" stroke-width="1.8"/>
        </svg>
        <span class="contact-text">mdorsey083651@quillpost.example</span>
      </li>
    </ul>
  </section>
</body>
</html>
```